Meridane Works, Inc. - Update our Website

Meridane Works needs a website to help our customers to navigate through our services efficiently. Our existing website is at www.meridwork.example

We would like to explain our services with content and pictures (photographs) that distinguishes our products and services from our competition.

The website design must implement a strategy to focus on our Contract Labeling services.

With this new design we would like to attract new customers and ensure that our existing customers are fully informed with our latest offerings.

```html
<!DOCTYPE html>
<html lang="en">
<head>
<meta charset="utf-8">
<title>Meridane Works, Inc.</title>
<link href="https://fonts.googleapis.com/css2?family=Roboto:wght@300;400;500;700&display=swap" rel="stylesheet">
<style>
:root{
  --ink:#333333;
  --muted:#555555;
  --white:#ffffff;
  --rule:#cfcfcf;
  --hero-top:#6fb6d8;
  --hero-bottom:#5aa6cf;
  --lime:#80d900;
  --orange:#ff6d00;
  --blue:#0081c1;
  --thumb:#dad8d8;
  --footer:#333333;
}
*{box-sizing:border-box;margin:0;padding:0}
html,body{width:1048px;height:1200px;overflow:hidden}
body{position:relative;background:var(--white);font-family:'Roboto',sans-serif;color:var(--ink)}
.site-header{position:absolute;left:0;top:0;width:1048px;height:29px;background:var(--white)}
.brand{position:absolute;left:208px;top:8px;display:flex;align-items:center;gap:5px;font-size:9px;font-weight:700;letter-spacing:.3px;color:var(--ink)}
.brand-dot{width:12px;height:12px;border-radius:50%;background:var(--lime)}
.main-nav{position:absolute;right:210px;top:9px;display:flex;gap:24px;font-size:9px;color:var(--muted)}
.hero{position:absolute;left:0;top:29px;width:1048px;height:391px;background:linear-gradient(180deg,var(--hero-top),var(--hero-bottom))}
.hero-person{position:absolute;left:476px;top:54px;width:319px;height:337px;border-radius:140px 140px 0 0;background:linear-gradient(180deg,rgba(255,255,255,.35),rgba(255,255,255,.6))}
.hero-title{position:absolute;left:207px;top:168px;font-size:29px;font-weight:300;color:var(--white);letter-spacing:.3px}
.hero-lead{position:absolute;left:207px;top:213px;width:330px;font-size:11.3px;line-height:15.3px;font-weight:300;color:var(--white)}
.hero-button{position:absolute;left:207px;top:277px;width:79px;height:30px;border:1.5px solid var(--white);color:var(--white);font-size:8.5px;font-weight:500;display:flex;align-items:center;justify-content:center}
.section-title{position:absolute;left:0;width:1048px;text-align:center;font-size:17.5px;font-weight:300;color:var(--ink)}
.section-rule{position:absolute;left:450px;width:149px;height:1.5px;background:var(--rule)}
.service-card{position:absolute;top:513px;width:202px}
.service-image{display:block;width:202px;height:153px}
.service-name{margin-top:15px;font-size:14px;font-weight:300;line-height:16px;letter-spacing:.2px}
.service-text{margin-top:6px;font-size:7.6px;line-height:11.6px}
.product{position:absolute;width:320px}
.product-thumb{position:absolute;left:0;top:0;width:78px;height:78px;background:var(--thumb)}
.product-body{position:absolute;left:91px;top:0;width:210px}
.product-name{font-size:14px;font-weight:300;line-height:16px;margin-top:-1px}
.product-text{margin-top:5px;font-size:7.6px;line-height:11.8px}
.site-footer{position:absolute;left:0;top:1154px;width:1048px;height:46px;background:var(--footer);color:var(--white);font-size:8.5px;font-weight:500;display:flex;align-items:center;justify-content:center}
</style>
</head>
<body>
<header class="site-header">
  <div class="brand"><span class="brand-dot"></span>MERIDANE WORKS INC.</div>
  <nav class="main-nav"><span>Home</span><span>Services</span><span>About Us</span><span>User Support</span><span>Contact Us</span></nav>
</header>

<section class="hero" role="img" aria-label="Blurred photograph of medicine bottles in blue tones">
  <div class="hero-person" role="img" aria-label="Photograph of a smiling lab technician in a white coat"></div>
</section>
<h1 class="hero-title">MERIDANE WORKS, INC.</h1>
<p class="hero-lead">Meridane Works, Inc. specializes in providing products and services to the pharmaceutical industry. We are focused on the needs of those individuals involved with Clinical Trial Materials.</p>
<div class="hero-button">SERVICES</div>

<h2 class="section-title" style="top:459px">Services</h2>
<div class="section-rule" style="top:492px"></div>

<article class="service-card" style="left:207px">
  <svg class="service-image" viewBox="0 0 202 153" role="img" aria-label="Service photograph placeholder"><rect width="202" height="153" fill="var(--lime)"/><path d="M0 0L202 153M202 0L0 153" stroke="#ffffff" stroke-opacity=".5" stroke-width="1"/></svg>
  <h3 class="service-name">MERISERV™</h3>
  <p class="service-text">MERISERV™ is a contract clinical label generation service that provides you with ready to apply clinical labels designed and produced for your specific clinical trial needs.</p>
</article>
<article class="service-card" style="left:422px">
  <svg class="service-image" viewBox="0 0 202 153" role="img" aria-label="Service photograph placeholder"><rect width="202" height="153" fill="var(--orange)"/><path d="M0 0L202 153M202 0L0 153" stroke="#ffffff" stroke-opacity=".5" stroke-width="1"/></svg>
  <h3 class="service-name">MERIBOOK™ CLINICAL<br>BOOKLET LABELS</h3>
  <p class="service-text">MERISERV™ is a contract clinical label generation service that provides you with ready to apply clinical labels designed and produced for your specific clinical trial needs.</p>
</article>
<article class="service-card" style="left:636px">
  <svg class="service-image" viewBox="0 0 202 153" role="img" aria-label="Service photograph placeholder"><rect width="202" height="153" fill="var(--blue)"/><path d="M0 0L202 153M202 0L0 153" stroke="#ffffff" stroke-opacity=".5" stroke-width="1"/></svg>
  <h3 class="service-name">CLINICAL RANDOMIZATION</h3>
  <p class="service-text">Our systems can create randomization data for all types of CTM requirements.</p>
</article>

<h2 class="section-title" style="top:807px">Software / Stock</h2>
<div class="section-rule" style="top:840px"></div>

<article class="product" style="left:207px;top:861px">
  <div class="product-thumb" role="img" aria-label="Product image placeholder"></div>
  <div class="product-body">
    <h3 class="product-name">MERIPRO/LBL™</h3>
    <p class="product-text">MERIPRO/LBL™ is the industry's leading clinical label generation system offering superior overall capability and flexibility.</p>
  </div>
</article>
<article class="product" style="left:524px;top:861px">
  <div class="product-thumb" role="img" aria-label="Product image placeholder"></div>
  <div class="product-body">
    <h3 class="product-name">SOFTWARE VALIDATION<br>SERVICE</h3>
    <p class="product-text">Our knowledge of pharmaceutical industry practices and standards along with regulatory requirements, enable us to create practical and cost-effective solutions for your validation needs.</p>
  </div>
</article>
<article class="product" style="left:207px;top:962px">
  <div class="product-thumb" role="img" aria-label="Product image placeholder"></div>
  <div class="product-body">
    <h3 class="product-name">MERISTOCK™</h3>
    <p class="product-text">MERISTOCK™ is a premium line of label stock products that we supply to the pharmaceutical industry.</p>
  </div>
</article>

<footer class="site-footer">© 2011 Meridane Works, Inc. All rights reserved.</footer>
</body>
</html>
```